Save the date: email notification

I need a "Save the Date" email notification design for my wedding:

Objetives:

1.- to notify friends about our future wedding ( by sending an email)
2.- to request our friends to send us their phisical address. ( reply to the email)

It will not be the formal invitation for the wedding, just an announcement.

Wedding Date: 15-sep-2012
Our names: Lucía & Rodrigo

Target Market(s)

friends, family and other commitments

Industry/Entity Type

Wedding

Requirements
Must have
• Wedding Date: 15-sep-2012
Our names: Lucía & Rodrigo

```html
<!DOCTYPE html>
<html lang="es">
<head>
<meta charset="utf-8">
<title>Reserva esta fecha — Lucía &amp; Rodrigo</title>
<link rel="stylesheet" href="https://fonts.googleapis.com/css2?family=Open+Sans:wght@400;600;700&family=Italianno&display=swap">
<style>
  :root {
    --page-bg: #ffffff;
    --card-bg: #f5f1e8;
    --band-green: #5a6b00;
    --band-green-soft: #66780a;
    --ink: #2e3300;
  }
  html, body {
    margin: 0;
    padding: 0;
    width: 1200px;
    height: 960px;
    overflow: hidden;
    background: var(--page-bg);
  }
  .canvas {
    position: relative;
    width: 1200px;
    height: 960px;
  }
  .save-the-date {
    position: absolute;
    left: 28px;
    top: 162px;
    width: 1145px;
    height: 654px;
    background: var(--card-bg);
    display: flex;
  }
  .side-band {
    width: 270px;
    height: 100%;
    background: linear-gradient(180deg, var(--band-green-soft), var(--band-green));
    flex: none;
  }
  .announcement {
    position: relative;
    flex: 1;
    color: var(--ink);
    text-align: center;
  }
  .announcement > * {
    position: absolute;
    left: 0;
    right: 0;
    margin: 0;
  }
  .headline {
    top: 49px;
    font-family: "Open Sans", sans-serif;
    font-weight: 700;
    font-size: 47px;
    letter-spacing: 5px;
  }
  .wedding-date {
    top: 125px;
    font-family: "Italianno", cursive;
    font-size: 54px;
    font-weight: 400;
  }
  .couple-names {
    top: 230px;
    font-family: "Italianno", cursive;
    font-size: 132px;
    font-weight: 400;
    line-height: 1;
  }
  .celebration {
    top: 452px;
    font-family: "Open Sans", sans-serif;
    font-size: 30px;
    font-weight: 400;
  }
  .rsvp {
    top: 527px;
    font-family: "Open Sans", sans-serif;
    font-size: 24px;
    letter-spacing: 1px;
  }
  .rsvp-note {
    top: 574px;
    font-family: "Open Sans", sans-serif;
    font-size: 17px;
    letter-spacing: 0.5px;
  }
</style>
</head>
<body>
<main class="canvas">
  <section class="save-the-date">
    <div class="side-band" role="img" aria-label="Franja verde decorada con círculos dobles color crema"></div>
    <div class="announcement">
      <h1 class="headline">RESERVA ESTA FECHA</h1>
      <p class="wedding-date">15 de Septiembre de 2012</p>
      <h2 class="couple-names">Lucía &amp; Rodrigo</h2>
      <p class="celebration">CELEBRAREMOS NUESTRA BODA</p>
      <p class="rsvp">S.R.C. a este email con tu direccion postal.</p>
      <p class="rsvp-note">En breve te haremos llegar nuestra invitacion.</p>
    </div>
  </section>
</main>
</body>
</html>
```